Landing Page Design

We need a landing page template designed to support a clients Zintro Bidlink Campaigns. The client is called Merrow Plumbing and they install and repair hot water systems (only). They provide no other plumbing services.

We are really looking for a great looking landing page that is both engaging and functional.

Target Market(s)

Residential/Domestic market. Typically wives and partners who are typically home or run the household.

Industry/Entity Type

Plumbing

Number of Pages Required

1 page

Requirements
Must have
• Strong branding
Strong call to actions
Great and obvious looking buttons
Nice to have
• Smart use of colour
Should not have
• The design should not use old-style, serif fonts.

Do not include any plumbing images

```html
<!DOCTYPE html>
<html lang="en">
<head>
<meta charset="utf-8">
<title>Merrow Plumbing – Hot Water Now</title>
<link rel="stylesheet" href="https://fonts.googleapis.com/css2?family=Arimo:wght@400;700&display=swap">
<style>
:root{
  --green-deep:#2f8a1c;
  --green-bright:#7fc926;
  --green-text:#1e5d14;
  --panel-top:#f6faf4;
  --panel-bottom:#a9d59a;
  --red:#e8261b;
  --orange:#f26a21;
  --orange-light:#f7931e;
  --white:#ffffff;
  --ink:#111111;
  --field-border:#9fb79a;
}
*{box-sizing:border-box;margin:0;padding:0}
html,body{width:1200px;height:914px;overflow:hidden}
body{
  position:relative;
  font-family:"Arimo",Arial,sans-serif;
  background:radial-gradient(ellipse at 20% 35%,#c8ec6a 0%,var(--green-bright) 35%,var(--green-deep) 100%);
}
.corner-ribbon{
  position:absolute;top:30px;right:-52px;width:240px;height:44px;
  background:var(--orange);color:var(--white);transform:rotate(45deg);
  display:flex;align-items:center;justify-content:center;text-align:center;
  font-weight:700;font-size:16px;line-height:17px;
}
.page-panel{
  position:absolute;left:131px;top:39px;width:938px;height:840px;
  border-radius:10px;overflow:hidden;
  background:linear-gradient(180deg,var(--panel-top) 0%,#e3f0de 25%,#c3e2b7 60%,var(--panel-bottom) 100%);
}
.page-header{position:absolute;left:0;top:0;width:100%;height:131px;border-bottom:1px solid #4e6a48;
  background:linear-gradient(180deg,#ffffff 0%,#e4f1df 100%)}
.brand{position:absolute;left:38px;top:50px;display:flex;align-items:center;gap:10px;
  font-weight:700;font-size:28px;color:var(--red)}
.brand-mark{width:18px;height:18px;border-radius:50%;background:var(--orange-light)}
.header-call{position:absolute;left:600px;width:320px;top:24px;text-align:center;color:var(--green-text);font-weight:700}
.header-call .lead{font-size:34px;line-height:38px}
.header-call .number{font-size:50px;line-height:56px}
.banner{
  position:absolute;left:117px;top:205px;width:514px;height:45px;
  background:linear-gradient(180deg,#f5411f,var(--red));color:var(--white);
  font-weight:700;font-size:32px;line-height:45px;padding-left:36px;
  box-shadow:3px 3px 4px rgba(0,0,0,.3);
}
.intro{position:absolute;left:24px;top:254px;width:340px}
.intro h1{font-size:31px;line-height:38px;color:var(--green-text);font-weight:700}
.intro .copy{margin:13px 0 0 28px;width:272px;font-size:16.5px;line-height:20px;color:var(--ink)}
.intro .copy p+p{margin-top:20px}
.photo{position:absolute;left:375px;top:254px;width:210px;height:347px;border:2px solid var(--white);
  background:linear-gradient(160deg,#d8d8d8 0%,#8a8a8a 45%,#c9a58e 100%);box-shadow:2px 2px 4px rgba(0,0,0,.25)}
.cta-button{
  position:absolute;width:290px;height:46px;color:var(--white);font-weight:700;font-size:21px;
  line-height:46px;padding-left:38px;text-decoration:none;
  background:linear-gradient(90deg,var(--red),var(--orange));box-shadow:3px 3px 4px rgba(0,0,0,.3);
}
.cta-quote{left:117px;top:701px}
.cta-site{left:117px;top:787px}
.benefits{position:absolute;left:754px;top:205px;width:288px;height:175px;border-radius:10px;
  border:2px solid #f8b36b;background:linear-gradient(180deg,var(--orange-light),var(--red));
  list-style:none;padding:12px 0 0 18px}
.benefits li{display:flex;align-items:center;gap:14px;height:30.5px;color:var(--white);font-weight:700;font-size:16.5px}
.tick{width:24px;height:22px;flex:none}
.offer{position:absolute;left:755px;top:393px;width:287px;height:82px;border-radius:10px;
  background:linear-gradient(180deg,#ffffff,#d9ecd2);text-align:center;color:var(--green-text);
  font-weight:700;font-size:15.5px;line-height:21px;padding-top:8px}
.offer .phone{color:var(--red)}
.enquiry-form{position:absolute;left:778px;top:483px;width:244px}
.enquiry-form label{display:block;font-style:italic;font-size:13.5px;color:var(--ink);height:18px;margin-top:3px}
.enquiry-form .field{display:block;width:240px;height:29px;border:1px solid var(--field-border);background:var(--white);margin-bottom:3px}
.enquiry-form .field-comments{height:57px}
.enquire-button{position:absolute;left:790px;top:823px;width:217px;height:38px;border-radius:7px;
  background:linear-gradient(180deg,#3fa94a,#0c6a2b);border:2px solid #b5d9aa;color:var(--white);
  font-weight:700;font-size:20px;text-align:center;line-height:34px}
.copyright{position:absolute;left:0;width:100%;top:888px;text-align:center;color:var(--white);font-size:10px}
</style>
</head>
<body>
<div class="corner-ribbon">Our Rebates<br>Information</div>

<main class="page-panel">
  <header class="page-header">
    <div class="brand"><span class="brand-mark"></span>Merrow Plumbing</div>
    <div class="header-call"><div class="lead">Call NOW on</div><div class="number">9417 5380</div></div>
  </header>

  <section class="intro">
    <h1>Solar Water Systems</h1>
    <div class="copy">
      <p>Switch to solar hot water and cut your energy bills! Supplied and installed by our licensed team. No fuss, no hidden costs.</p>
      <p>To take advantage of this great offer call us on 1300 58 71 40 or complete and submit the form on this page.</p>
      <p>At Merrow we look after all your hot water needs - painlessly. We understand that hot water should simply be there when you need it. A set and forget proposition.</p>
    </div>
  </section>

  <div class="photo" role="img" aria-label="Photo of a woman enjoying a hot shower"></div>
</main>

<div class="banner">HOT WATER NOW! SAVE $$$</div>
<a class="cta-button cta-quote">Book a FREE Quote</a>
<a class="cta-button cta-site">Visit Our Web Site</a>

<ul class="benefits">
  <li><svg class="tick" viewBox="0 0 24 22"><rect x="1" y="5" width="16" height="16" fill="#f4a15a" stroke="#fff" stroke-width="1.5"/><path d="M5 12l5 6L22 2" fill="none" stroke="#fff" stroke-width="3"/></svg>Sydney 24 Hours 7 Days</li>
  <li><svg class="tick" viewBox="0 0 24 22"><rect x="1" y="5" width="16" height="16" fill="#f4a15a" stroke="#fff" stroke-width="1.5"/><path d="M5 12l5 6L22 2" fill="none" stroke="#fff" stroke-width="3"/></svg>On Time</li>
  <li><svg class="tick" viewBox="0 0 24 22"><rect x="1" y="5" width="16" height="16" fill="#f4a15a" stroke="#fff" stroke-width="1.5"/><path d="M5 12l5 6L22 2" fill="none" stroke="#fff" stroke-width="3"/></svg>Professional Technicians</li>
  <li><svg class="tick" viewBox="0 0 24 22"><rect x="1" y="5" width="16" height="16" fill="#f4a15a" stroke="#fff" stroke-width="1.5"/><path d="M5 12l5 6L22 2" fill="none" stroke="#fff" stroke-width="3"/></svg>We Advise on Rebates</li>
  <li><svg class="tick" viewBox="0 0 24 22"><rect x="1" y="5" width="16" height="16" fill="#f4a15a" stroke="#fff" stroke-width="1.5"/><path d="M5 12l5 6L22 2" fill="none" stroke="#fff" stroke-width="3"/></svg>Authorised Kelvo Dealer</li>
</ul>

<div class="offer">Take advantage of this great offer.<br>Contact Us NOW on <span class="phone">9417 5380</span><br>or register your interest below:</div>

<form class="enquiry-form">
  <label>Your First Name:</label><span class="field"></span>
  <label>Your Surname:</label><span class="field"></span>
  <label>Your Suburb:</label><span class="field"></span>
  <label>Best Contact Number:</label><span class="field"></span>
  <label>Your Email Address:</label><span class="field"></span>
  <label>Enquiry / Comments</label><span class="field field-comments"></span>
</form>
<div class="enquire-button">ENQUIRE NOW</div>

<footer class="copyright">Copyright 2010 Merrow Plumbing Hot Water Solutions</footer>
</body>
</html>
```